Business card design for new, innovative company - BluePlinth

We are a new company looking for a business card design that is fun, different and quirky. Must use corporate colour green - CMYK C:55, M:0, Y:100, K:0, and corporate colour grey - C:0, M:0, Y: 0, K:70.

We have developed the first real time data application, in which people are able to profile the data of their existing customers in order to pull out more good fit clients to direct their marketing activities at.

Industry/Entity Type

Marketing

Requirements
Must have
• Logo, name, title, telephone number, fax number, email, website, address

```html
<!DOCTYPE html>
<html lang="en">
<head>
<meta charset="utf-8">
<title>BluePlinth business card</title>
<link rel="stylesheet" href="https://fonts.googleapis.com/css2?family=Montserrat:wght@400;600;800&display=swap">
<style>
  :root {
    --brand-green: #7ac143;
    --brand-grey: #6d6e71;
    --pattern-green: #72b63c;
    --card-white: #ffffff;
    --backdrop: #e9e9e9;
    --text-font: "Montserrat", Arial, sans-serif;
  }
  html, body {
    margin: 0;
    width: 1200px;
    height: 900px;
    overflow: hidden;
    background: var(--backdrop);
    font-family: var(--text-font);
  }
  .stage {
    position: relative;
    width: 1200px;
    height: 900px;
  }
  .card {
    position: absolute;
    width: 580px;
    height: 350px;
    border-radius: 30px;
    overflow: hidden;
    box-shadow: 0 6px 18px rgba(0,0,0,0.12);
  }

  /* Front of card */
  .card-front {
    left: 540px;
    top: 90px;
    background: var(--card-white);
  }
  .front-logo {
    position: absolute;
    left: 38px;
    top: 30px;
    margin: 0;
    font-size: 52px;
    font-weight: 800;
    letter-spacing: -1.5px;
    color: var(--brand-green);
  }
  .person-name {
    position: absolute;
    left: 40px;
    top: 122px;
    margin: 0;
    font-size: 25px;
    font-weight: 400;
    letter-spacing: 0.5px;
    color: var(--brand-grey);
  }
  .person-name .first-name {
    font-weight: 800;
    color: var(--brand-green);
  }
  .contact-list {
    position: absolute;
    left: 40px;
    top: 170px;
    margin: 0;
    padding: 0;
    list-style: none;
    font-size: 15px;
    line-height: 24px;
    color: var(--brand-grey);
  }
  .contact-list .label {
    color: var(--brand-green);
  }
  .address {
    position: absolute;
    left: 345px;
    top: 222px;
    margin: 0;
    font-style: normal;
    font-size: 14px;
    line-height: 22px;
    color: var(--brand-grey);
  }
  .address .web {
    color: var(--brand-green);
  }
  .front-bands {
    position: absolute;
    left: 0;
    bottom: 0;
    width: 580px;
    height: 90px;
  }

  /* Back of card */
  .card-back {
    left: 80px;
    top: 460px;
    background: var(--brand-green);
  }
  .back-pattern {
    position: absolute;
    inset: 0;
    background: linear-gradient(160deg, var(--brand-green), var(--pattern-green));
  }
  .back-logo {
    position: absolute;
    left: 0;
    right: 0;
    top: 118px;
    margin: 0;
    text-align: center;
    font-size: 70px;
    font-weight: 800;
    letter-spacing: -2px;
    color: var(--card-white);
  }
  .back-web {
    position: absolute;
    left: 0;
    right: 0;
    top: 222px;
    margin: 0;
    text-align: center;
    font-size: 17px;
    font-weight: 600;
    letter-spacing: 1.5px;
    color: var(--card-white);
  }
</style>
</head>
<body>
<main class="stage">

  <section class="card card-front" aria-label="Card front">
    <h1 class="front-logo">BluePlinth</h1>
    <h2 class="person-name"><span class="first-name">JOANNA</span> PELLING</h2>
    <ul class="contact-list">
      <li><span class="label">M:</span> 07700900462</li>
      <li><span class="label">T:</span> 01632 960518</li>
      <li><span class="label">E:</span> joanna.pelling@tidemarkdata.com</li>
    </ul>
    <address class="address">
      22c Fenmoor Road,<br>
      Ely, Cambridgeshire, CB7 4QT<br>
      <span class="web">www.blueplinth.com</span>
    </address>
    <svg class="front-bands" viewBox="0 0 580 90" aria-hidden="true">
      <path d="M0 48 H300 L330 78 H580 V84 H326 L296 54 H0 Z" fill="var(--brand-green)"/>
      <path d="M0 60 H292 L322 90 H0 Z" fill="var(--brand-grey)"/>
    </svg>
  </section>

  <section class="card card-back" aria-label="Card back">
    <div class="back-pattern" role="img" aria-label="Repeating company-name texture in a slightly darker green"></div>
    <h1 class="back-logo">BluePlinth</h1>
    <p class="back-web">www.blueplinth.com</p>
  </section>

</main>
</body>
</html>
```